Meridale Freightworks Group - needs a website

Build a simple but professional website for Meridale Freightworks Group.
Web address is www.merfregro.com.au
We have just completed developing a brochure and the contents of the brochure would serve as the web pages.
Web design does not need to deviate far from the brochure and will not include electronic commerce etc at this stage.

Target Market(s)

Privately owned logistics businesses in Australia

Industry/Entity Type

Build

Number of Pages Required

5+ page

Requirements
Must have
• Professional, elegant, ability to upload video in the future, ability to add e-commerce in the future

```html
<!DOCTYPE html>
<html lang="en">
<head>
<meta charset="utf-8">
<title>Meridale Freightworks Group</title>
<link href="https://fonts.googleapis.com/css2?family=Exo+2:wght@400;500;600;700&family=Roboto:wght@300;400;500&display=swap" rel="stylesheet">
<style>
:root{
  --brand-blue:#1a4f8f;
  --band-blue:#17518f;
  --text-dark:#2b2b2b;
  --text-grey:#6f6f6f;
  --line-grey:#cfcfcf;
  --footer-bg:#2a2a2a;
  --footer-text:#bdbdbd;
  --white:#ffffff;
  --play-red:#d8202a;
}
*{margin:0;padding:0;box-sizing:border-box}
html,body{width:794px;height:1200px;overflow:hidden;background:var(--white)}
body{position:relative;font-family:"Roboto",Arial,sans-serif;color:var(--text-dark)}
.abs{position:absolute}

/* header */
.site-header{position:absolute;left:0;top:0;width:794px;height:70px;background:var(--white)}
.brand{left:88px;top:22px;display:flex;align-items:center;gap:6px;font-family:"Exo 2",sans-serif;font-weight:700;font-size:13px;color:var(--brand-blue);line-height:1.05;width:150px}
.brand-dot{width:14px;height:14px;border-radius:50%;background:var(--brand-blue);flex:none}
.header-contact{right:88px;top:14px;font-size:9px;color:var(--text-grey);display:flex;align-items:center;gap:3px}
.header-contact strong{font-weight:400;font-size:10.5px;color:#111}
.main-nav{right:88px;top:38px;display:flex;gap:0;font-size:8px;color:var(--text-grey)}
.main-nav a{text-decoration:none;color:inherit;padding:4px 9px;border:1px solid transparent;border-radius:2px;margin-left:1px}
.main-nav a.active{border-color:var(--brand-blue);color:var(--brand-blue)}

/* hero */
.hero{left:0;top:70px;width:794px;height:254px;background:linear-gradient(100deg,#6b5a3a 0%,#c8a86a 30%,#e3d2a8 55%,#efe5cc 75%,#d9c9a0 100%)}
.hero-tagline{right:88px;top:208px;font-family:"Exo 2",sans-serif;font-weight:500;font-size:22px;color:var(--white);letter-spacing:.3px;text-shadow:0 1px 3px rgba(0,0,0,.35)}
.hero-dots{left:378px;top:233px;display:flex;gap:5px}
.hero-dots span{width:6px;height:6px;border-radius:50%;background:var(--white)}
.hero-dots span.on{background:transparent;border:1px solid var(--white)}

/* intro */
.intro-title{left:0;width:794px;top:355px;text-align:center;font-family:"Exo 2",sans-serif;font-weight:600;font-size:21px;color:var(--brand-blue)}
.intro-lead{left:0;width:794px;top:388px;text-align:center;font-size:10.5px;color:#333}
.intro-body{left:88px;width:618px;top:410px;text-align:center;font-size:7.4px;line-height:13.8px;color:var(--text-grey)}
.video-divider{left:88px;width:618px;top:464px;display:flex;align-items:center;gap:10px;font-family:"Exo 2",sans-serif;font-size:11px;color:#333}
.video-divider::before,.video-divider::after{content:"";flex:1;height:1px;background:var(--line-grey)}
.video-frame{left:250px;top:493px;width:292px;height:157px;background:radial-gradient(ellipse at 50% 30%,#a49a86 0%,#5e4f3e 45%,#2e2a25 100%)}
.play-btn{left:124px;top:63px}

/* features */
.feature-band{left:0;top:696px;width:794px;height:196px;background:var(--band-blue)}
.feature{position:absolute;top:26px;width:126px;text-align:center;color:var(--white)}
.feature-icon{width:52px;height:52px;border-radius:50%;background:var(--white);margin:0 auto;display:flex;align-items:center;justify-content:center}
.feature h3{font-family:"Exo 2",sans-serif;font-weight:400;font-size:17px;margin-top:9px;letter-spacing:.3px}
.feature p{font-size:6px;line-height:10.6px;color:#c9d6e8;margin-top:5px}
.feature a{display:inline-block;margin-top:8px;font-size:6.4px;color:var(--white);text-decoration:underline}

/* news */
.news-title{left:88px;top:928px;font-family:"Exo 2",sans-serif;font-weight:600;font-size:20px;color:var(--brand-blue)}
.news-arrows{left:683px;top:936px;display:flex;border:1px solid #ccc;border-radius:2px}
.news-arrows span{width:11px;height:11px;display:flex;align-items:center;justify-content:center}
.news-arrows span+span{border-left:1px solid #ccc}
.news-card{position:absolute;top:964px;width:147px;height:76px;border:1px solid #ddd;background:var(--white);box-shadow:0 3px 5px rgba(0,0,0,.08);padding:12px 12px}
.news-card p{font-size:6.6px;line-height:10.4px;color:#333}
.news-date{display:inline-block;margin-top:6px;background:#eee;font-size:5.8px;color:#666;padding:3px 6px;border-radius:1px}

/* footer */
.site-footer{left:0;top:1088px;width:794px;height:112px;background:var(--footer-bg);color:var(--footer-text)}
.footer-col{position:absolute;top:20px}
.footer-col h4{font-family:"Roboto",sans-serif;font-weight:300;font-size:9.5px;color:#eee;margin-bottom:9px}
.contact-list li{list-style:none;display:flex;align-items:center;gap:10px;font-size:7px;height:18px}
.contact-list svg{width:9px;flex:none}
.footer-divider{position:absolute;top:22px;width:1px;height:68px;background:#444}
.footer-nav{display:grid;grid-template-columns:70px 74px 60px;row-gap:9px;font-size:7px}
.footer-nav span::before{content:"• ";color:#888}
.footer-brand{font-family:"Roboto",sans-serif;font-weight:500;font-size:11px;color:#8a8a8a;display:flex;align-items:center;gap:6px}
.footer-brand i{width:11px;height:11px;border-radius:50%;background:#8a8a8a;display:block}
.footer-copy{font-size:7px;line-height:18px;margin-top:10px}
</style>
</head>
<body>

<header class="site-header">
  <div class="abs brand"><span class="brand-dot"></span><span>Meridale Freightworks Group</span></div>
  <div class="abs header-contact">
    <svg width="8" height="8" viewBox="0 0 24 24"><path fill="#333" d="M6.6 10.8a15 15 0 0 0 6.6 6.6l2.2-2.2c.3-.3.7-.4 1-.2 1.1.4 2.3.6 3.6.6.6 0 1 .4 1 1V20c0 .6-.4 1-1 1A17 17 0 0 1 3 4c0-.6.4-1 1-1h3.5c.6 0 1 .4 1 1 0 1.3.2 2.5.6 3.6.1.3 0 .7-.2 1z"/></svg>
    Contact us : <strong>07 5550 1840</strong>
  </div>
  <nav class="abs main-nav">
    <a class="active" href="#">Home</a><a href="#">About us</a><a href="#">Solutions</a><a href="#">How it works</a><a href="#">Benefits</a><a href="#">Our Team</a><a href="#">Contact us</a>
  </nav>
</header>

<section class="abs hero" role="img" aria-label="Warehouse interior with forklifts and tall stocked pallet racking">
  <div class="abs hero-tagline">Scale &nbsp;:&nbsp; Synergy &nbsp;:&nbsp; Value</div>
  <div class="abs hero-dots"><span class="on"></span><span></span><span></span><span></span></div>
</section>

<h1 class="abs intro-title">A new solution for Australian warehouse business owners</h1>
<p class="abs intro-lead">Offering national scale to increase revenues, achieving synergie to reduce costs, and enhancing the value in your business.</p>
<p class="abs intro-body">Aenean faucibus lacus ut mollis commodo. Donec vestibulum odio sem, ac laoreet massa ullamcorper id. Donec molestie nisi et tellus hendrerit vehicula. Nunc eu ligula sed quam pulvinar maximus in vitae eros. Proin porta fermentum ipsum, vel porttitor turpis venenatis luctus. Vivamus volutpat eu sapien quis tempus. Aenean feugiat viverra lorem ac sagit tis. Donec sit amet lectus nec mi tempor laoreet ac nec nunc. Duis id auctor sapien.</p>

<div class="abs video-divider">View our video to know how it works</div>
<div class="abs video-frame" role="img" aria-label="Video still of a long warehouse aisle between orange pallet racks">
  <svg class="abs play-btn" width="44" height="31" viewBox="0 0 44 31"><rect width="44" height="31" rx="7" fill="var(--play-red)"/><path d="M17 9 L29 15.5 L17 22 Z" fill="#fff"/></svg>
</div>

<section class="abs feature-band">
  <div class="feature" style="left:87px">
    <div class="feature-icon"><svg width="22" height="18" viewBox="0 0 22 18"><path d="M1 1V17H21" stroke="var(--band-blue)" stroke-width="2" fill="none"/><rect x="5" y="8" width="2.5" height="7" fill="var(--band-blue)"/><rect x="9" y="4" width="2.5" height="11" fill="var(--band-blue)"/><rect x="13" y="9" width="2.5" height="6" fill="var(--band-blue)"/><rect x="17" y="6" width="2.5" height="9" fill="var(--band-blue)"/></svg></div>
    <h3>SCALE</h3>
    <p>Nunc sit amet consequat risus. Curabitur ac elit leo. In eleifend dui tellus, in scelerisque elit porttitor integer eu massa lacinia, lacinia nulla non, volutpat purus.</p>
    <a href="#">READ MORE</a>
  </div>
  <div class="feature" style="left:251px">
    <div class="feature-icon"><svg width="24" height="18" viewBox="0 0 24 18"><circle cx="12" cy="4.5" r="3.5" fill="var(--band-blue)"/><circle cx="5" cy="6" r="2.6" fill="var(--band-blue)"/><circle cx="19" cy="6" r="2.6" fill="var(--band-blue)"/><path d="M6 17c0-4 2.7-7 6-7s6 3 6 7z" fill="var(--band-blue)"/><path d="M0 16c0-3 2-5 5-5 1 0 1.8.2 2.4.6C5.8 13 5 14.6 5 16z" fill="var(--band-blue)"/><path d="M24 16c0-3-2-5-5-5-1 0-1.8.2-2.4.6 1.6 1.4 2.4 3 2.4 4.4z" fill="var(--band-blue)"/></svg></div>
    <h3>SYNERGY</h3>
    <p>Nunc sit amet consequat risus. Curabitur ac elit leo. In eleifend dui tellus, in scelerisque elit porttitor integer eu massa lacinia, lacinia nulla non, volutpat purus.</p>
    <a href="#">READ MORE</a>
  </div>
  <div class="feature" style="left:415px">
    <div class="feature-icon"><svg width="24" height="18" viewBox="0 0 24 18"><path d="M1 1V17H23" stroke="var(--band-blue)" stroke-width="2" fill="none"/><path d="M4 13 L9 8 L13 11 L20 4" stroke="var(--band-blue)" stroke-width="2.2" fill="none"/><path d="M16 3 H21 V8" stroke="var(--band-blue)" stroke-width="2" fill="none"/></svg></div>
    <h3>VALUE</h3>
    <p>Nunc sit amet consequat risus. Curabitur ac elit leo. In eleifend dui tellus, in scelerisque elit porttitor integer eu massa lacinia, lacinia nulla non, volutpat purus.</p>
    <a href="#">READ MORE</a>
  </div>
  <div class="feature" style="left:579px">
    <div class="feature-icon"><svg width="22" height="18" viewBox="0 0 22 18"><path d="M8 2H3a2 2 0 0 0-2 2v10a2 2 0 0 0 2 2h5" stroke="var(--band-blue)" stroke-width="2.2" fill="none"/><path d="M7 6.5h6V2.5L21 9l-8 6.5v-4H7z" fill="var(--band-blue)"/></svg></div>
    <h3>POTENTIAL EXIT</h3>
    <p>Nunc sit amet consequat risus. Curabitur ac elit leo. In eleifend dui tellus, in scelerisque elit porttitor integer eu massa lacinia, lacinia nulla non, volutpat purus.</p>
    <a href="#">READ MORE</a>
  </div>
</section>

<h2 class="abs news-title">Latest News</h2>
<div class="abs news-arrows">
  <span><svg width="4" height="5" viewBox="0 0 4 5"><path d="M4 0L0 2.5 4 5z" fill="#999"/></svg></span>
  <span><svg width="4" height="5" viewBox="0 0 4 5"><path d="M0 0l4 2.5L0 5z" fill="#999"/></svg></span>
</div>
<article class="news-card" style="left:88px"><p>Donec vestibulum odio sem, ac laoreet massa ullamcorper id. Donec molestie nisi et tellus hendrerit vehicula.</p><span class="news-date">25 November, 2015</span></article>
<article class="news-card" style="left:245px"><p>Donec vestibulum odio sem, ac laoreet massa ullamcorper id. Donec molestie nisi et tellus hendrerit vehicula.</p><span class="news-date">25 November, 2015</span></article>
<article class="news-card" style="left:402px"><p>Donec vestibulum odio sem, ac laoreet massa ullamcorper id. Donec molestie nisi et tellus hendrerit vehicula.</p><span class="news-date">25 November, 2015</span></article>
<article class="news-card" style="left:559px"><p>Donec vestibulum odio sem, ac laoreet massa ullamcorper id. Donec molestie nisi et tellus hendrerit vehicula.</p><span class="news-date">25 November, 2015</span></article>

<footer class="abs site-footer">
  <div class="footer-col" style="left:88px">
    <h4>Contact us</h4>
    <ul class="contact-list">
      <li><svg viewBox="0 0 24 24"><path fill="#aaa" d="M6.6 10.8a15 15 0 0 0 6.6 6.6l2.2-2.2c.3-.3.7-.4 1-.2 1.1.4 2.3.6 3.6.6.6 0 1 .4 1 1V20c0 .6-.4 1-1 1A17 17 0 0 1 3 4c0-.6.4-1 1-1h3.5c.6 0 1 .4 1 1 0 1.3.2 2.5.6 3.6.1.3 0 .7-.2 1z"/></svg>07 5550 1840</li>
      <li><svg viewBox="0 0 24 24"><rect x="6" y="2" width="12" height="20" rx="2" fill="#aaa"/><rect x="8" y="5" width="8" height="12" fill="var(--footer-bg)"/></svg>0400 555 219</li>
      <li><svg viewBox="0 0 24 24"><rect x="2" y="5" width="20" height="14" rx="1" fill="#aaa"/><path d="M2 6l10 7 10-7" stroke="var(--footer-bg)" stroke-width="2" fill="none"/></svg>ellis.marsh@merfregro.com.au</li>
    </ul>
  </div>
  <div class="footer-divider" style="left:249px"></div>
  <div class="footer-col" style="left:283px">
    <h4>Navigation Links</h4>
    <div class="footer-nav">
      <span>Home</span><span>How it works</span><span>Contact us</span>
      <span>About us</span><span>Benefits</span><span>Sitemap</span>
      <span>Solutions</span><span>Our Team</span>
    </div>
  </div>
  <div class="footer-divider" style="left:501px"></div>
  <div class="footer-col" style="left:540px;top:28px">
    <div class="footer-brand"><i></i>Meridale Freightworks Group</div>
    <p class="footer-copy">Copyright © 2015 Meridale Freightworks Group<br>All rights reserved.</p>
  </div>
</footer>

</body>
</html>
```